Store Front Window Design

We have a beautiful corner store front dental practice with no window signage. Crazy I know...that's why we need your help.

The final design will be done in all vinyl unless unless you suggest a different medium (meaning we are open to some design idea like using frosted glass, etc...).

The windows provide a lot of natural light so the design needs to keep a lot of natural light coming into the office. Keep in mind vinyl is not opaque so keep the signage aesthetically pleasing and a minimalist design to allow as much natural light in as possible. The design should follow the aesthetic from our logo. or tie into at least. We want a cohesive brand aesthetic.

I submitted some general layout ideas. There is a blue banner with advertising words which we want to be used in the final version. Even though the lettering is black, in reality the letters will be a white vinyl on the outside of the window. When you submit your work, be sure to add any special instructions (aka tell me the vision for the letters is white not black, maybe gold leaf, or forested glass...stuff like that). AND YOU DO NOT HAVE TO FOLLOW MY PATTERN! YOU ARE ARTISTS AND WE ARE LOOKING FOR AN ARTISTIC EYE CATCHING PRESENTATION OF THIS INFORMATION. MAKE IT FLASHY AND ADD SOME AESTHETIC FROM THE TOOTH LOGO.

The store front is 6 windows roughly 60'' x 36'' The smaller windows below are 27'' x 36''. Around the corner there are 3 windows. they are 60'' x 27'' lower windows are 27" x 27". We would like to keep the bottom windows clear and keep the signage on the top windows, however, we are flexible.

The front 6 windows need to have this information worked into the design.

Practice name: Vesk and Ormond Dental & Orthodontics.
Phone numbers: Marisol Vesk DDS: 415.772.0183
Tobias Ormond DDS:415.509.2371

Expertise: Dr. Vesk General Dentistry & Orthodontics
Dr. Ormond Oral Surgery & Sedation

Address: 1937 Birchwood Ave

A banner across the bottom of the top windows with some key advertisement words: "Clarivet" "Braces" "Implants" "Whiting" "Call today" "Free Consultation" "Oral Surgery" "Sedation". We like the two color idea. Its up to you to decide on the color combo. I used a Dark and light blue, but maybe a Blue and grey would nice to tire in the logo colors?

I have made some mock ideas to get the ball rolling but you do not have to stick to these designs at all, just as long as all the required information is there. Be creative with the layouts, fonts, color scheme, (just remember these are going on windows not necessarily a white background), and graphics/artistic flare (refer to logo for layout inspiration and use the logo as an actual graphic). We are running a miltimillion dollar dental practice so we want these windows to be eye catching to pull in patients and look like a million dollar design. Also all 6 windows dont need ot be used. I am really looking for creative design marketing.

The corner 3 windows need the following information: name, expertise, phone number, banner.

Dr. Vesk, General Dentistry & Orthodontics, 415.772.0183
Dr. Ormond, Oral Surgery & Sedation, 415.509.2371

There is also a front door that needs to be designed. The door is 60'' x 36'' (standard door size) We want simple white vinyl on the outside of the door. We need you to organize the information on the door, pick a easy to read font, maybe use the logo and use some of the front window signage aesthetic? Its up to you...but we we were initially thinking of just making the litters white and keep it simple but again you are the designers.

Practice name: Vesk and Ormond General Dentistry & Orthodontics

Address: 1937 Birchwood Ave

Phone numbers: Dr. Vesk 415.772.0183
Dr. Ormond 415.509.2371

Hours of operation: Mon: call for an appointment
Tues-Thurs: 9am-5pm
Sat: call for an appointment
Sun: Closed

A line saying we speak Spanish: Se Habla Espanol

*****************************************************************************************************
here are some design that we liked and some rough sketches I made to start the ball rolling. Keep in mind that there are 9 windows for the front because its a corner office, but not all of them have to have stuff on it. We want simple, streamline, classy high commanding price point aesthetic. I am hiring you for your artistic minds.

Target Market(s)

anyone who has dental needs

Industry/Entity Type

Dental

Font styles to use
Serif
Sans Serif

Colors

Designer to choose colors to be used in the design.

Requirements
Must have
• 1. The required information (see project description)
• 2. Logo
• 3. Advertisement banner running along the bottom of all 9 windows (6 in front and 3 on the side)
• NOTE: Look at pictures of the store to get a sense of the customers point of view and also as a reference to how your design will be broken up across several windows or maybe you design something special for every window. But we want the banner to run along all the windows to lead customs to the door on the side. Finally the letters will be done in white vinyl unless state otherwise, remember the window needs to let in natural light so the entire window can not be covered in vinyl.
Nice to have
• artistic flare yet simple and sleep and expensive looking aesthetic. work logo into the design.
Should not have
• The goal is to catch someone eye and give them important information about the practice.
• It should not just be words.
• It should not have to many words
• It must be readable font for cards driving by.

```html
<!DOCTYPE html>
<html lang="en">
<head>
<meta charset="utf-8">
<title>Vesk and Ormond Dental &amp; Orthodontics – Door Signage</title>
<link rel="stylesheet" href="https://fonts.googleapis.com/css2?family=Montserrat:wght@500;600;700&family=Roboto+Condensed:wght@700&display=swap">
<style>
  :root {
    --backdrop: #f1f1f1;
    --panel: #ffffff;
    --brand-blue: #1273c4;
    --deep-teal: #1b5f72;
    --soft-teal: #4a98a6;
    --band-teal: #4a97a3;
    --brand-grey: #8f9091;
    --white: #ffffff;
  }
  * { margin: 0; padding: 0; box-sizing: border-box; }
  html, body {
    width: 1200px; height: 1200px; overflow: hidden;
    background: var(--backdrop);
    font-family: "Montserrat", Arial, sans-serif;
  }
  .door-panel {
    position: absolute; left: 238px; top: 0;
    width: 721px; height: 1200px;
    background: var(--panel);
  }
  .brand {
    position: absolute; left: 0; top: 34px; width: 100%;
    text-align: center;
  }
  .brand-dot {
    display: block; margin: 0 auto 22px;
    width: 110px; height: 110px; border-radius: 50%;
    background: var(--brand-grey);
  }
  .brand-name {
    color: var(--brand-grey);
    font-weight: 600; font-size: 22px; line-height: 1.25;
    letter-spacing: 0.5px;
  }
  .info { position: absolute; left: 80px; right: 80px; }
  .address {
    top: 262px; color: var(--brand-blue);
    font-weight: 700; font-size: 54px; line-height: 60px;
    white-space: nowrap;
  }
  .doctor {
    position: absolute; left: 80px;
    color: var(--deep-teal); font-weight: 600;
    font-size: 48px; line-height: 56px;
  }
  .phone {
    position: absolute; left: 80px;
    display: flex; align-items: center; gap: 14px;
    color: var(--soft-teal); font-weight: 500;
    font-size: 38px; line-height: 44px;
  }
  .phone svg { width: 38px; height: 38px; flex: none; }
  .divider {
    position: absolute; left: 80px; top: 607px;
    width: 555px; height: 2px; background: var(--soft-teal);
  }
  .day {
    position: absolute; left: 78px;
    color: var(--deep-teal); font-weight: 600;
    font-size: 40px; line-height: 46px;
  }
  .hours {
    position: absolute; left: 78px;
    color: var(--soft-teal); font-weight: 500;
    font-size: 37px; line-height: 44px;
  }
  .spanish-band {
    position: absolute; left: 0; top: 1066px;
    width: 100%; height: 114px;
    background: var(--band-teal);
    display: flex; align-items: center; justify-content: center;
    color: var(--white);
    font-family: "Roboto Condensed", "Arial Narrow", sans-serif;
    font-weight: 700; font-size: 64px; letter-spacing: 2px;
  }
  .base-strip {
    position: absolute; left: 0; top: 1180px;
    width: 100%; height: 20px; background: var(--deep-teal);
  }
</style>
</head>
<body>
  <main class="door-panel">
    <header class="brand">
      <span class="brand-dot"></span>
      <p class="brand-name">Vesk and Ormond<br>Dental &amp; Orthodontics</p>
    </header>

    <p class="info address">1937 Birchwood Ave</p>

    <p class="doctor" style="top:350px">Dr. Vesk</p>
    <p class="phone" style="top:416px">
      <svg viewBox="0 0 40 40" aria-hidden="true"><circle cx="20" cy="20" r="18" fill="none" stroke="currentColor" stroke-width="2.5"/><path d="M16 10c-3 2-4 6-3 10s4 8 8 10l3-4-4-3-2 2c-2-2-3-4-3-7l3-1-1-5z" fill="currentColor"/></svg>
      (415)772-0183
    </p>
    <p class="doctor" style="top:470px">Dr. Ormond</p>
    <p class="phone" style="top:536px">
      <svg viewBox="0 0 40 40" aria-hidden="true"><circle cx="20" cy="20" r="18" fill="none" stroke="currentColor" stroke-width="2.5"/><path d="M16 10c-3 2-4 6-3 10s4 8 8 10l3-4-4-3-2 2c-2-2-3-4-3-7l3-1-1-5z" fill="currentColor"/></svg>
      (415)509-2371
    </p>

    <div class="divider"></div>

    <p class="day" style="top:623px">Monday</p>
    <p class="hours" style="top:672px">call for an appointment</p>
    <p class="day" style="top:734px">Tuesday-Thursday</p>
    <p class="hours" style="top:784px">9:00 am to 5:00 pm</p>
    <p class="day" style="top:846px">Saturday</p>
    <p class="hours" style="top:896px">call for an appointment</p>
    <p class="day" style="top:951px">Sunday</p>
    <p class="hours" style="top:1002px">Closed</p>

    <div class="spanish-band">Se Habla Espanol</div>
    <div class="base-strip"></div>
  </main>
</body>
</html>
```